Tralvo GmbH banner ad

Banner ad for Facebook Our company name (logo) Title: Transporter and bus rental Text: Without deposit, super prices

Target Market(s)

Rental

Requirements
Must have
• LOGO from us, Evt. A pair of transporters in the picture

```html
<!DOCTYPE html>
<html lang="de">
<head>
<meta charset="utf-8">
<title>Tralvo GmbH – Banner</title>
<link href="https://fonts.googleapis.com/css2?family=Roboto+Condensed:wght@300;700&display=swap" rel="stylesheet">
<style>
  :root {
    --page-bg: #eeeeee;
    --navy: #0b0b6e;
    --steel-blue: #8ea4c0;
    --panel-top: #ffffff;
    --panel-bottom: #d9d9dc;
    --glass-teal: #3f6f78;
    --glass-light: #86a9ad;
    --van-white: #eff2f3;
    --van-shade: #d3d8db;
    --bumper-grey: #4a5358;
    --road-grey: #8f979b;
  }
  html, body {
    margin: 0;
    width: 1200px;
    height: 1200px;
    overflow: hidden;
    background: var(--page-bg);
  }
  .banner {
    position: absolute;
    left: 0;
    top: 286px;
    width: 1200px;
    height: 628px;
    display: block;
  }
  .brand-name {
    font-family: "Roboto Condensed", sans-serif;
    font-weight: 700;
    font-size: 66px;
    fill: var(--navy);
  }
  .headline {
    font-family: "Roboto Condensed", sans-serif;
    font-weight: 700;
    font-size: 54px;
    letter-spacing: -0.6px;
    fill: var(--navy);
  }
  .tagline {
    font-family: "Roboto Condensed", sans-serif;
    font-weight: 300;
    font-size: 56px;
    letter-spacing: -0.6px;
    fill: var(--steel-blue);
  }
</style>
</head>
<body>
<svg class="banner" viewBox="0 0 1200 628" xmlns="http://www.w3.org/2000/svg">
  <defs>
    <linearGradient id="fleetTone" x1="0" y1="0" x2="0.3" y2="1">
      <stop offset="0" stop-color="var(--glass-teal)"/>
      <stop offset="0.14" stop-color="var(--glass-light)"/>
      <stop offset="0.26" stop-color="var(--van-white)"/>
      <stop offset="0.5" stop-color="var(--van-shade)"/>
      <stop offset="0.66" stop-color="#7d878c"/>
      <stop offset="0.8" stop-color="var(--bumper-grey)"/>
      <stop offset="1" stop-color="var(--road-grey)"/>
    </linearGradient>
    <linearGradient id="panelTone" x1="0" y1="0" x2="0" y2="1">
      <stop offset="0" stop-color="var(--panel-top)"/>
      <stop offset="1" stop-color="var(--panel-bottom)"/>
    </linearGradient>
  </defs>

  <rect class="fleet-photo" x="0" y="0" width="1200" height="628" fill="url(#fleetTone)"
        role="img" aria-label="Foto: Reihe weißer Transporter schräg von vorn auf einem nassen Parkplatz"/>

  <g class="brand">
    <rect x="50" y="198" width="52" height="52" fill="var(--navy)"/>
    <text class="brand-name" x="118" y="248">Tralvo GmbH</text>
  </g>

  <g class="bottom-panel">
    <polygon class="accent-wedge" points="0,628 100,327 129,372 31,628" fill="var(--steel-blue)"/>
    <polygon class="navy-band" points="100,327 1200,532 1200,545 129,372" fill="var(--navy)"/>
    <polygon class="text-panel" points="129,372 1200,545 1200,628 31,628" fill="url(#panelTone)"/>
  </g>

  <text class="headline" x="100" y="518">Transporter und Bus Vermietung</text>
  <text class="tagline" x="98" y="582">Ohne Kaution, Superpreise</text>
</svg>
</body>
</html>
```